Orvelle Massage website required

We need a website for a mobile sports massage therapist in the United Kingdom. Specialising in pregnancy and postnatal massage, sports and remedial, deep tissue massage & Corprate Massage. Attached are some logos that we already have in various colours. The file named logo_white_background is what we normally use. Feel free to use the others at your discretion.

Requirements
Must have
• Service areas, Booking system.

```html
<!DOCTYPE html>
<html lang="en">
<head>
<meta charset="UTF-8">
<title>Orvelle Massage — Footer</title>
<link rel="stylesheet" href="https://fonts.googleapis.com/css2?family=Open+Sans:wght@400&display=swap">
<style>
  :root {
    --ink-navy: #25222f;
    --paper: #ffffff;
    --muted-grey: #9b9b9b;
    --chevron: #8d8b96;
  }
  html, body {
    margin: 0;
    padding: 0;
    overflow: hidden;
    background: var(--paper);
  }
  .site-footer {
    position: relative;
    width: 1200px;
    height: 292px;
    overflow: hidden;
    background: var(--paper);
    font-family: "Open Sans", Arial, sans-serif;
  }
  .footer-backdrop {
    position: absolute;
    inset: 0;
    display: block;
  }
  .brand-name {
    position: absolute;
    top: 139px;
    left: 0;
    width: 1200px;
    margin: 0;
    text-align: center;
    font-size: 16px;
    font-weight: 400;
    color: var(--ink-navy);
    letter-spacing: 0.02em;
  }
  .footer-nav {
    position: absolute;
    top: 200px;
    left: 0;
    width: 1200px;
    display: flex;
    justify-content: center;
    gap: 46px;
    margin: 0;
    padding: 0;
    list-style: none;
  }
  .footer-nav a {
    font-size: 14.5px;
    color: var(--muted-grey);
    text-decoration: none;
    text-transform: uppercase;
  }
  .footer-legal {
    position: absolute;
    top: 235px;
    left: 0;
    width: 1200px;
    margin: 0;
    text-align: center;
    font-size: 14.5px;
    color: var(--muted-grey);
    text-transform: uppercase;
  }
</style>
</head>
<body>
  <footer class="site-footer">
    <svg class="footer-backdrop" width="1200" height="292" viewBox="0 0 1200 292" aria-hidden="true">
      <path fill="var(--ink-navy)" d="M0 0 H1200 V146 L264 30 C200 22 142 50 98 108 L0 204 Z"/>
      <circle cx="600" cy="67" r="22" fill="var(--ink-navy)"/>
      <polyline points="590,69 600,78 610,69" fill="none" stroke="var(--chevron)" stroke-width="1.2"/>
    </svg>

    <p class="brand-name">Orvelle Massage</p>

    <ul class="footer-nav">
      <li><a href="#">Home</a></li>
      <li><a href="#">About us</a></li>
      <li><a href="#">Service</a></li>
      <li><a href="#">Gallery</a></li>
      <li><a href="#">Contacts</a></li>
    </ul>

    <p class="footer-legal">@2018. Privacy policy</p>
  </footer>
</body>
</html>
```